Painting Valtoni Renovations New buildings

Paint jobs plasterwork renovations new building customer painter paper drywall Entsorgungen.neukunden win color splash pleasure in colors competent clean fast reliable new try build demolition color combinations color concepts offers washing façade painting wood stains new projects old building renovations yes no beautiful new old sell secure solve paint over paint paint spray paint lye assemble disassemble sell buy trade oil dust new old assembly disassembly putty sanding fashion devastation copying belief feng shui kleopatra pompes beer colors swamp lime abrasion release tighten

Target Market(s)

construction industry

Contact Information for Business Card

Maler

Font styles to use
Serif

Colors
f04a50
959595

Requirements
Must have
• elegant appearance
Nice to have
• simply goal-oriented clientele in detail
Should not have
• too colorful

```html
<!DOCTYPE html>
<html lang="en">
<head>
<meta charset="utf-8">
<title>Valtoni – Business Card</title>
<link rel="stylesheet" href="https://fonts.googleapis.com/css2?family=Inter:wght@400;500;700&display=swap">
<style>
  :root {
    --backdrop: #5f5f5f;
    --card: #ffffff;
    --accent: #e5484d;
    --ink: #3a3a3a;
    --brand: #1d4a8c;
  }
  html, body {
    margin: 0;
    padding: 0;
    width: 1200px;
    height: 1200px;
    overflow: hidden;
    background: var(--backdrop);
    font-family: "Inter", Arial, sans-serif;
  }
  .card {
    position: absolute;
    left: 169px;
    top: 349px;
    width: 862px;
    height: 502px;
    background: var(--card);
    border-radius: 30px;
  }
  .brand {
    position: absolute;
    left: 62px;
    top: 215px;
    display: flex;
    align-items: center;
    gap: 16px;
    color: var(--brand);
  }
  .brand-dot {
    width: 26px;
    height: 26px;
    border-radius: 50%;
    background: var(--brand);
  }
  .brand-name {
    font-size: 72px;
    font-weight: 700;
    line-height: 1;
    letter-spacing: -1px;
  }
  .details {
    position: absolute;
    right: 33px;
    top: 0;
    text-align: right;
    color: var(--ink);
  }
  .person-name {
    position: absolute;
    right: 0;
    top: 102px;
    margin: 0;
    white-space: nowrap;
    font-size: 34px;
    font-weight: 500;
    color: var(--accent);
  }
  .person-role {
    position: absolute;
    right: 0;
    top: 150px;
    margin: 0;
    font-size: 22px;
    white-space: nowrap;
  }
  .contact {
    position: absolute;
    right: 0;
    margin: 0;
    font-size: 20px;
    white-space: nowrap;
  }
  .address-1 { top: 290px; }
  .address-2 { top: 317px; }
  .phone     { top: 361px; }
  .email     { top: 395px; }
  .web       { top: 431px; }
  .web .accent { color: var(--accent); }
</style>
</head>
<body>
  <div class="card">
    <div class="brand">
      <span class="brand-dot"></span>
      <span class="brand-name">Valtoni</span>
    </div>
    <div class="details">
      <p class="person-name">Lena Hartwig</p>
      <p class="person-role">Manager</p>
      <p class="contact address-1">18 Juniper Lane</p>
      <p class="contact address-2">Northmead Lakeside Gauteng 1620</p>
      <p class="contact phone">010 555 0142</p>
      <p class="contact email">hello@valtonipaint.co.za</p>
      <p class="contact web">www.<span class="accent">valtonipaint</span>.co.za</p>
    </div>
  </div>
</body>
</html>
```